We are an Estate agency (Real estate)– looking for Christmas/winter theme leaflet

We are called ‘’HOLLWICKS’’ we are an estate agency based in England. We opened in 2020 in February, few weeks before Covid and we are now known as one of the fastest growing agencies in all of Brighton and Hove.
This is our first Christmas/winter leaflet and this kind of offer!
Offer is: if the client signs with us to sell their home from 1st December 2021 until 7th January 2022 they will receive 50% off HOLLWICKS fees.
I am looking for A5 two-sided leaflet. The first side should contain our branding, the offer. Also, maybe this: ‘’ Let us Treat you this Christmas’’ or maybe on the other side of leaflet, which will contain explanation of the offer, our office details etc. the back should also contain some design.
Our target market is higher end clients who own a property in Brighton and Hove and looking to sell. I would say target market 35+ years of age.
Our branding is clean, fresh and eye catching and that’s what leaflet should look like and represent.
I will insert our website link so you could have a look at the properties that we deal with too. I could also insert last leaflet which I designed and had a really positive response & feedback… maybe will give you some ideas.
I have inserted our brand guidelines. We use Hollwicks in white or blue backgrounds as in guideline.
https://www.hollwicksestateagents.co.uk/
Hi guys,
Thank you for all your ideas so far, however just wanted to mention that I am looking for not so much ''in your face Christmas'' design - something subtle.
Needs to be classy, modern and eye catching - our target market is property owners 35+ years of age. Moreover, this offer needs to be perceived as one off opportunity.
35+ property owners

```html
<!DOCTYPE html>
<html lang="en">
<head>
<meta charset="utf-8">
<title>Hollwicks – Christmas Leaflet</title>
<link href="https://fonts.googleapis.com/css2?family=Ubuntu:wght@400;500;700&display=swap" rel="stylesheet">
<style>
  :root {
    --navy: #0a2845;
    --red: #c4000b;
    --red-deep: #a10006;
    --magenta: #d8168c;
    --white: #ffffff;
    --page: #ffffff;
  }
  * { box-sizing: border-box; margin: 0; padding: 0; }
  html, body { width: 1200px; height: 900px; overflow: hidden; background: var(--page); }
  body { font-family: "Ubuntu", sans-serif; color: var(--white); }
  .stage { position: relative; width: 1200px; height: 900px; }

  .panel { position: absolute; top: 147px; width: 447px; height: 634px; background: var(--navy); overflow: hidden; }
  .panel--offer { left: 159px; }
  .panel--cover { left: 617px; }

  /* Brand mark */
  .brand-square { position: absolute; border: 2px solid var(--white); }
  .brand-name { position: absolute; font-weight: 500; letter-spacing: 0.2em; text-align: center; white-space: nowrap; }
  .panel--offer .brand-square { left: 48px; top: 19px; width: 36px; height: 46px; }
  .panel--offer .brand-name { left: 6px; width: 120px; top: 80px; font-size: 12.5px; }

  /* Photo strip */
  .accent-bar { position: absolute; left: 0; top: 115px; width: 42px; height: 330px; background: linear-gradient(180deg, var(--red-deep), #b50008); }
  .photo-strip { position: absolute; left: 50px; top: 115px; width: 124px; height: 330px; display: flex; flex-direction: column; gap: 1px; }
  .photo { flex: 1; }
  .photo--1 { background: linear-gradient(180deg, #7fa4cf 0%, #e7ebe9 55%, #7b8a6a 100%); }
  .photo--2 { background: linear-gradient(180deg, #dfe8f2 0%, #a8503d 45%, #e6e4de 80%, #8a8074 100%); }
  .photo--3 { background: linear-gradient(180deg, #7fa8dd 0%, #b45c43 50%, #577a45 85%, #a79a8a 100%); }
  .photo--4 { background: linear-gradient(180deg, #c9d6e4 0%, #a9533f 45%, #4f6b37 80%, #9b7a5c 100%); }

  /* Headline */
  .headline { position: absolute; right: 17px; top: 22px; text-align: right; color: var(--red); font-weight: 700; font-size: 82px; line-height: 63px; letter-spacing: -0.01em; }
  .offer-terms { position: absolute; right: 17px; top: 217px; width: 240px; text-align: right; font-size: 15.5px; line-height: 21px; }

  /* About */
  .divider-rule { position: absolute; left: 206px; top: 304px; width: 3px; height: 308px; background: var(--red); }
  .about { position: absolute; left: 227px; top: 301px; width: 205px; }
  .about-title { color: var(--red); font-weight: 700; font-size: 14px; line-height: 18px; white-space: nowrap; letter-spacing: -0.02em; }
  .about-text { font-size: 11.6px; line-height: 18.1px; text-align: justify; margin-top: 0; }

  /* Contact */
  .contact-icons { position: absolute; left: 224px; top: 560px; width: 18px; display: flex; flex-direction: column; gap: 3px; }
  .contact-icons svg { width: 17px; height: 14px; }
  .contact-box { position: absolute; left: 248px; top: 558px; width: 199px; height: 53px; background: var(--red-deep); text-align: right; padding: 5px 11px 0 0; }
  .contact-phone { font-weight: 700; font-size: 14px; line-height: 17px; }
  .contact-line { font-size: 10.6px; line-height: 13px; }

  /* Office */
  .office { position: absolute; left: 20px; top: 487px; width: 180px; }
  .office-heading { font-weight: 700; font-size: 12px; line-height: 14px; }
  .office-line { font-size: 10.3px; line-height: 17px; }
  .office-block + .office-block { margin-top: 12px; }

  /* Cover */
  .cover-lines { position: absolute; inset: 0; }
  .cover-slogan { position: absolute; left: 21px; top: 188px; transform-origin: 0 0; transform: rotate(-37deg) translateY(-44px); font-weight: 700; font-size: 58px; line-height: 51px; white-space: nowrap; letter-spacing: -0.01em; }
  .cover-slogan .is-accent { color: var(--red-deep); }
  .panel--cover .brand-square { left: 198px; top: 461px; width: 50px; height: 63px; border: 3px solid var(--magenta); }
  .panel--cover .brand-name { left: 0; width: 447px; top: 547px; font-size: 17px; }
</style>
</head>
<body>
<main class="stage">

  <section class="panel panel--offer">
    <div class="brand-square"></div>
    <div class="brand-name">HOLLWICKS</div>

    <div class="accent-bar"></div>
    <div class="photo-strip">
      <div class="photo photo--1" role="img" aria-label="White period townhouse on a sunny street"></div>
      <div class="photo photo--2" role="img" aria-label="Red-brick Victorian house with white bay windows"></div>
      <div class="photo photo--3" role="img" aria-label="Red-brick detached family home"></div>
      <div class="photo photo--4" role="img" aria-label="Edwardian red-brick house with front garden"></div>
    </div>

    <h1 class="headline">SELL<br>YOUR<br>HOME</h1>
    <p class="offer-terms">from 1st December 2021 until 7th January 2022and receive and 50% off HOLLWICKS fees</p>

    <div class="divider-rule"></div>
    <div class="about">
      <h2 class="about-title">THINKING OF MOVING HOME?</h2>
      <p class="about-text">We have created an estate agency which offers a first class personal service with an honest and friendly approach. Having been open for only a year we have earned a name as one of the fastest growing estate agents in all Brighton &amp; Hove. Hollwicks are extremely active in generating sales and achieving record breaking prices on premium properties in Hove. We have several serious buyers who are keen to purchase a property in the Hove area.</p>
    </div>

    <div class="contact-icons" aria-hidden="true">
      <svg viewBox="0 0 17 14"><path d="M3 1 L6 1 L7 4 L5.5 5.5 Q7.5 9 11 10.5 L12.5 9 L15.5 10 L15.5 13 Q8 13.5 3 6.5 Q1.5 3.5 3 1 Z" fill="#fff"/></svg>
      <svg viewBox="0 0 17 14"><rect x="1" y="2" width="15" height="10" fill="none" stroke="#fff" stroke-width="1.3"/><path d="M1 2 L8.5 8 L16 2 M1 12 L6.5 6.5 M16 12 L10.5 6.5" fill="none" stroke="#fff" stroke-width="1.1"/></svg>
      <svg viewBox="0 0 17 14"><circle cx="8.5" cy="7" r="6" fill="none" stroke="#fff" stroke-width="1.1"/><ellipse cx="8.5" cy="7" rx="2.6" ry="6" fill="none" stroke="#fff" stroke-width="1"/><path d="M2.5 7 H14.5 M3.5 4 H13.5 M3.5 10 H13.5" stroke="#fff" stroke-width="0.9"/></svg>
    </div>
    <div class="contact-box">
      <div class="contact-phone">01273 555 018</div>
      <div class="contact-line">sales@hollwicksestateagents.co.uk</div>
      <div class="contact-line">www.hollwicksestateagents.co.uk</div>
    </div>

    <div class="office">
      <div class="office-block">
        <h3 class="office-heading">OUR OFFICE</h3>
        <p class="office-line">48 Western Rd, Hove, BN3 1AF</p>
      </div>
      <div class="office-block">
        <h3 class="office-heading">OPENING TIMES</h3>
        <p class="office-line">Monday to Friday: 8.45am - 6:30pm</p>
        <p class="office-line">Saturday: 8.45am - 5pm</p>
        <p class="office-line">Sunday: By appointment only</p>
        <p class="office-line">Open 7 days a week</p>
      </div>
    </div>
  </section>

  <section class="panel panel--cover">
    <svg class="cover-lines" viewBox="0 0 447 634" aria-hidden="true">
      <polyline points="0,178 164,401" fill="none" stroke="var(--magenta)" stroke-width="4"/>
      <polyline points="0,527 340,274 447,421" fill="none" stroke="var(--magenta)" stroke-width="4"/>
    </svg>
    <h2 class="cover-slogan">LET US<br>TREAT<br>YOU<br>THIS<br><span class="is-accent">CHRISTMAS</span></h2>
    <div class="brand-square"></div>
    <div class="brand-name">HOLLWICKS</div>
  </section>

</main>
</body>
</html>
```